BrookvaleLogic Website Design

To design a website for BrookvaleLogic, a software development company. The website should reflect the branding of our company, which is Smart, Beautiful, and Sophisticated. The existing website is www.brookvalelogic-example.com.sg

```html
<!DOCTYPE html>
<html lang="en">
<head>
<meta charset="utf-8">
<title>BrookvaleLogic</title>
<link href="https://fonts.googleapis.com/css2?family=Open+Sans:wght@300;400;600;700&display=swap" rel="stylesheet">
<style>
:root{
  --blue:#2a8fd0;
  --blue-btn:#2b9ad6;
  --navy:#0a3550;
  --navy-deep:#06263b;
  --text:#333;
  --muted:#555;
  --white:#fff;
  --tile-border:#e2e2e2;
}
*{margin:0;padding:0;box-sizing:border-box}
html,body{width:771px;height:1200px;overflow:hidden;background:var(--white);font-family:'Open Sans',sans-serif;color:var(--text)}
.canvas{position:relative;width:771px;height:1200px}
.abs{position:absolute}
.header{top:0;left:0;width:771px;height:48px;background:var(--white)}
.brand{left:106px;top:12px;display:flex;align-items:center;gap:6px;font-size:15px;font-weight:600;color:var(--blue)}
.brand-dot{width:24px;height:24px;border-radius:50%;background:var(--navy)}
.nav{top:48px;left:0;width:771px;height:35px;background:linear-gradient(var(--navy),#0b4564);border-top:2px solid var(--blue)}
.nav ul{list-style:none;position:absolute;left:106px;top:0;display:flex;height:33px}
.nav li{font-size:8px;font-weight:700;color:var(--white);line-height:33px;padding:0 10px}
.nav li.active{background:var(--blue);padding:0 12px}
.hero{top:83px;left:0;width:771px;height:220px;background:radial-gradient(ellipse at 50% 40%,#1f6f94 0%,#0d4766 45%,var(--navy-deep) 100%)}
.tablet{left:149px;top:36px;width:186px;height:143px;background:#111;border-radius:6px;border:2px solid #333}
.tablet-screen{position:absolute;left:15px;top:13px;width:153px;height:109px;background:var(--white);display:flex;align-items:center;justify-content:center;gap:5px;font-size:13px;font-weight:600;color:var(--blue)}
.hero-box{left:365px;top:60px;width:289px;height:90px;background:rgba(2,20,32,.88);color:var(--white);font-size:14px;font-weight:300;line-height:21px;padding:12px 8px}
.dots{left:363px;top:197px;display:flex;gap:3px}
.dots span{width:9px;height:9px;border-radius:50%;background:var(--white)}
.dots span:first-child{background:var(--blue)}
.section-title{left:0;width:771px;text-align:center;font-size:14px;font-weight:400;color:var(--blue)}
.intro{left:106px;top:342px;width:559px;text-align:center;font-size:10.4px;line-height:18px;color:var(--muted)}
.card{width:178px}
.card-photo{height:102px}
.card p{font-size:7.6px;line-height:14px;color:var(--muted);margin-top:15px}
.btn{display:inline-block;margin-top:14px;background:var(--blue-btn);color:var(--white);font-size:8px;font-weight:700;padding:0 11px;line-height:23px;height:23px}
.logos{left:111px;top:686px;display:grid;grid-template-columns:repeat(8,63px);gap:5px 6px}
.tile{height:46px;border:1px solid var(--tile-border);box-shadow:0 1px 2px rgba(0,0,0,.12);display:flex;align-items:center;justify-content:center;font-size:9px;font-weight:700;color:#444}
.testi{width:180px}
.avatar{width:60px;height:60px;border-radius:50%;border:2px solid #ddd}
.who{position:absolute;left:69px;top:20px}
.who b{display:block;font-size:10.5px;font-weight:700;color:#333}
.who span{font-size:7.6px;color:var(--muted)}
.quote{font-size:24px;font-weight:700;color:#333;line-height:14px;margin-top:8px;height:14px}
.testi p{font-size:7.6px;line-height:14px;color:var(--muted);margin-top:2px}
.footer{top:1000px;left:0;width:771px;height:200px;background:radial-gradient(ellipse at 50% 20%,#0f5474 0%,var(--navy) 55%,var(--navy-deep) 100%);color:var(--white)}
.fcol h3{font-size:10.5px;font-weight:400;margin-bottom:12px}
.fcol ul{list-style:none}
.fcol li{font-size:8px;line-height:14.2px}
.fcol p{font-size:7.6px;line-height:12px}
.field{width:132px;height:16px;background:var(--white);border:1px solid #bbb;font-size:6.5px;color:#aaa;padding:3px 4px;margin-top:9px}
.subscribe{margin:7px 0 0 74px;width:58px;height:14px;border-radius:7px;background:var(--navy-deep);font-size:8px;font-weight:700;text-align:center;line-height:14px}
.social{display:flex;align-items:center;justify-content:space-between;width:86px;height:30px;font-size:8px}
.social i{width:23px;height:23px;border-radius:50%;background:#3aa7dd;display:block}
.copyright{top:177px;left:0;width:771px;text-align:center;font-size:7.6px}
</style>
</head>
<body>
<div class="canvas">
  <header class="header abs">
    <div class="brand abs"><span class="brand-dot"></span>BrookvaleLogic</div>
  </header>
  <nav class="nav abs">
    <ul>
      <li class="active">Home</li><li>About Us</li><li>The Team</li><li>Board Of Directors</li><li>Products And Services</li><li>Giving Back To Society</li><li>Contact Us</li><li>Locate Us</li>
    </ul>
  </nav>
  <section class="hero abs">
    <div class="tablet abs"><div class="tablet-screen"><span class="brand-dot"></span>BrookvaleLogic</div></div>
    <div class="hero-box abs">We enable languge translation audiio over text,video,animation and value added info in our interactive magazines</div>
    <div class="dots abs"><span></span><span></span><span></span><span></span></div>
  </section>

  <h2 class="section-title abs" style="top:321px">Products And Services</h2>
  <p class="intro abs">We design and develop customized and generic media centered software and mobile applications for companies and organizations with hosting and maintenance services options.</p>

  <div class="card abs" style="left:106px;top:402px">
    <div class="card-photo" role="img" aria-label="Hands typing on a keyboard" style="background:linear-gradient(135deg,#c9d3db,#6f8496)"></div>
    <p>Lorem Ipsum is simply dummy text of the printing and typesetting industry. Lorem Ipsum has been the industry's standard</p>
    <span class="btn">Read More</span>
  </div>
  <div class="card abs" style="left:296px;top:402px">
    <div class="card-photo" role="img" aria-label="Screens showing web designs" style="background:linear-gradient(135deg,#eef3f7,#a9c3d6)"></div>
    <p>Lorem Ipsum is simply dummy text of the printing and typesetting industry. Lorem Ipsum has been the industry's standard</p>
    <span class="btn">Read More</span>
  </div>
  <div class="card abs" style="left:486px;top:402px">
    <div class="card-photo" role="img" aria-label="Businesswoman with digital interface" style="background:linear-gradient(135deg,#8fb7cc,#2f5f7e)"></div>
    <p>Lorem Ipsum is simply dummy text of the printing and typesetting industry. Lorem Ipsum has been the industry's standard</p>
    <span class="btn">Read More</span>
  </div>

  <h2 class="section-title abs" style="top:656px">Company logos</h2>
  <div class="logos abs">
    <div class="tile">Ardentel</div><div class="tile">Bramwell</div><div class="tile">Corvex</div><div class="tile">Daltrix</div>
    <div class="tile">Elmgrove</div><div class="tile">Fennick</div><div class="tile">Galvor</div><div class="tile">Harlowe</div>
    <div class="tile">Istrum</div><div class="tile">Jorvane</div><div class="tile">Kessly</div><div class="tile">Lumora</div>
    <div class="tile">Marquel</div><div class="tile">Norbit</div><div class="tile">Ostiva</div><div class="tile">Pellan</div>
  </div>

  <h2 class="section-title abs" style="top:825px">Client Testimonials</h2>
  <div class="testi abs" style="left:106px;top:864px">
    <div class="avatar" role="img" aria-label="Client portrait" style="background:linear-gradient(#d9c2ad,#7a6452)"></div>
    <div class="who"><b>Martin Ellery</b><span>Company name</span></div>
    <div class="quote">&ldquo;</div>
    <p>Lorem Ipsum is simply dummy text of the printing and typesetting industry. Lorem Ipsum has been the industry's standard</p>
  </div>
  <div class="testi abs" style="left:295px;top:864px">
    <div class="avatar" role="img" aria-label="Client portrait" style="background:linear-gradient(#e7c9b0,#d2452b)"></div>
    <div class="who"><b>Martin Ellery</b><span>Company name</span></div>
    <div class="quote">&ldquo;</div>
    <p>Lorem Ipsum is simply dummy text of the printing and typesetting industry. Lorem Ipsum has been the industry's standard</p>
  </div>
  <div class="testi abs" style="left:485px;top:864px">
    <div class="avatar" role="img" aria-label="Client portrait" style="background:linear-gradient(#c7582f,#5a2a1a)"></div>
    <div class="who"><b>Martin Ellery</b><span>Company name</span></div>
    <div class="quote">&ldquo;</div>
    <p>Lorem Ipsum is simply dummy text of the printing and typesetting industry. Lorem Ipsum has been the industry's standard</p>
  </div>

  <footer class="footer abs">
    <div class="fcol abs" style="left:106px;top:16px">
      <h3>Quick Links</h3>
      <ul><li>Home</li><li>About Us</li><li>The Team</li><li>Board Of Directors</li><li>Products And Services</li><li>Giving Back To Society</li><li>Contact Us</li><li>Locate Us</li></ul>
    </div>
    <div class="fcol abs" style="left:250px;top:16px">
      <h3>Support Links</h3>
      <ul><li>Legal Notice</li><li>Privacy Policy</li><li>Terms &amp; Conditions</li><li>Help</li></ul>
    </div>
    <div class="fcol abs" style="left:393px;top:16px">
      <h3>Newsletter SignUp</h3>
      <p>Sign-up for our daily emails by<br>entering your information below:</p>
      <div class="field">Name</div>
      <div class="field">Enter Your E-Mail ID</div>
      <div class="subscribe">Subscribe</div>
    </div>
    <div class="fcol abs" style="left:582px;top:16px">
      <h3>Connect With Us</h3>
      <div class="social">Chirpline<i></i></div>
      <div class="social">Facepage<i style="background:#2d5ba8"></i></div>
      <div class="social">Vidstream<i style="background:#e23a2a"></i></div>
      <div class="social">Snapframe<i style="background:#8fb4cf"></i></div>
    </div>
    <div class="copyright abs">Copyright ©2013 Company Name &nbsp;- All rights reserved</div>
  </footer>
</div>
</body>
</html>
```